Business Card Design - Law Firm

We are a boutique law firm located near the beach in Manly, Australia. We have recently had a new logo designed and are revamping our business cards with the new logo.

We have recently had a business card design done for us but are not entirely happy with it. We are looking for something modern, simplistic but striking. We would like to see multiple designs.

We have attached a word document which includes our new logo and the current business card design which we are looking at moving away from.

We would like the business cards to be double sided. We would like the design to include something which we can print in gloss colour when we send it to the business card printers.

```html
<!DOCTYPE html>
<html lang="en">
<head>
<meta charset="utf-8">
<title>Whitfield &amp; Partners – Business Card</title>
<link rel="stylesheet" href="https://fonts.googleapis.com/css2?family=Open+Sans:wght@300;400;600;700&display=swap">
<style>
  :root {
    --ink: #1c1c1e;
    --navy: #2a3a8c;
    --navy-deep: #1f2b70;
    --navy-soft: #7f8fcf;
    --gold: #b29c63;
    --paper: #f4f4f4;
    --backdrop: #d9dadc;
    --muted: #4a4a4a;
  }
  * { box-sizing: border-box; margin: 0; padding: 0; }
  html, body {
    width: 1200px; height: 1021px; overflow: hidden;
    background: var(--backdrop);
    font-family: "Open Sans", sans-serif;
  }
  .stage { position: relative; width: 1200px; height: 1021px; }
  .card {
    position: absolute; width: 640px; height: 391px;
    border-radius: 4px; overflow: hidden;
    box-shadow: 0 14px 30px rgba(0,0,0,.22);
  }

  /* reverse side */
  .card--back {
    left: 430px; top: 90px;
    background: var(--navy);
  }
  .back-artwork {
    position: absolute; left: 0; top: 0; width: 640px; height: 300px;
    background:
      radial-gradient(ellipse 260px 150px at 150px 90px, rgba(160,175,230,.55), rgba(160,175,230,0) 70%),
      radial-gradient(ellipse 520px 110px at 400px 210px, rgba(31,43,112,.75), rgba(31,43,112,0) 75%),
      linear-gradient(180deg, rgba(255,255,255,.06), rgba(255,255,255,0));
  }
  .card--back .firm {
    position: absolute; right: 48px; bottom: 44px;
    color: #ffffff; text-align: right;
  }
  .card--back .firm-name {
    display: flex; align-items: center; justify-content: flex-end; gap: 12px;
    font-weight: 700; font-size: 30px; letter-spacing: 1px; line-height: 1.2;
  }
  .card--back .tagline {
    font-weight: 300; font-size: 15px; letter-spacing: 12px;
    margin-top: 4px; margin-right: 70px;
  }

  /* front side */
  .card--front {
    left: 130px; top: 530px;
    background: var(--paper);
    display: flex; align-items: center;
  }
  .brand {
    width: 310px; padding-left: 24px; display: flex; flex-direction: column; align-items: center;
  }
  .brand .firm-name {
    display: flex; align-items: center; gap: 10px;
    color: var(--navy); font-weight: 700; font-size: 22px; line-height: 1.2;
  }
  .brand .tagline {
    color: var(--muted); font-weight: 300; font-size: 12px; letter-spacing: 10px;
    margin-top: 6px; padding-left: 10px;
  }
  .mark-dot { width: 14px; height: 14px; border-radius: 50%; background: var(--navy); flex: none; }
  .card--back .mark-dot { width: 16px; height: 16px; background: #ffffff; }
  .divider { width: 1px; height: 175px; background: var(--gold); margin-left: 10px; }
  .contact { padding-left: 26px; color: var(--ink); }
  .contact .name { color: var(--navy); font-weight: 700; font-size: 24px; line-height: 1.1; }
  .contact .role { font-size: 16px; color: var(--muted); margin-bottom: 14px; }
  .contact .address { font-size: 16px; line-height: 1.3; margin-bottom: 4px; }
  .contact .line { display: flex; align-items: center; gap: 8px; font-size: 16px; line-height: 1.4; }
  .contact .line svg { width: 14px; height: 14px; flex: none; }
</style>
</head>
<body>
<main class="stage">
  <section class="card card--back" aria-label="Card reverse">
    <div class="back-artwork" role="img" aria-label="Large flowing wave decoration in light and deep blue tones"></div>
    <div class="firm">
      <p class="firm-name"><span class="mark-dot"></span>Whitfield &amp; Partners</p>
      <p class="tagline">LAWYERS</p>
    </div>
  </section>

  <section class="card card--front" aria-label="Card front">
    <div class="brand">
      <p class="firm-name"><span class="mark-dot"></span>Whitfield &amp; Partners</p>
      <p class="tagline">LAWYERS</p>
    </div>
    <div class="divider"></div>
    <div class="contact">
      <p class="name">Nora Ellison</p>
      <p class="role">Practice Manager</p>
      <p class="address">Suite 4, 12 Ocean Lane<br>CORALBAY NSW 2999</p>
      <p class="line">
        <svg viewBox="0 0 16 16" aria-hidden="true"><path fill="#b29c63" d="M3.5 1.5l2.5 0 1 3.5-1.8 1.2a8 8 0 0 0 4.6 4.6L11 9l3.5 1v2.5c0 1-1 2-2 2C6.5 14.5 1.5 9.5 1.5 3.5c0-1 1-2 2-2z"/></svg>
        (02) 5550 1834
      </p>
      <p class="line">
        <svg viewBox="0 0 16 16" aria-hidden="true"><rect x="1.5" y="3.5" width="13" height="9" fill="none" stroke="#b29c63" stroke-width="1.4"/><path d="M1.5 3.5l6.5 5 6.5-5" fill="none" stroke="#b29c63" stroke-width="1.4"/></svg>
        nora.ellison@bayfrontlaw.com.au
      </p>
      <p class="line">
        <svg viewBox="0 0 16 16" aria-hidden="true"><g fill="none" stroke="#b29c63" stroke-width="1.3"><circle cx="8" cy="8" r="6.3"/><ellipse cx="8" cy="8" rx="2.8" ry="6.3"/><path d="M1.7 8h12.6M2.8 4.8h10.4M2.8 11.2h10.4"/></g></svg>
        www.whitfieldpartners.com.au
      </p>
    </div>
  </section>
</main>
</body>
</html>
```